Freelancers in the field of IT security and IT service need a business card design

I need a business card design for my company. I am a freelancer and active in the area of IT security, IT support% 26 # 252; tung, consulting. I am not yet color-coded, but it should be a modern color that can also be used for a later website. The design should be innovation. Exude dynamism and reliability

Target Market(s)

IT security, IT solutions

Contact Information for Business Card

Firma: brandel-advisory, Inhaber: Jonas Wirtel
Adresse: Lindenhang 4, D-73218 Hollenried
Telefon: +49 (0) 7354 608193
E-Mail Jonas.Wirtel@brandel-advisory.example

```html
<!DOCTYPE html>
<html lang="de">
<head>
<meta charset="utf-8">
<title>brandel-advisory – Visitenkarte</title>
<link href="https://fonts.googleapis.com/css2?family=Montserrat:wght@400;500;700&display=swap" rel="stylesheet">
<style>
  :root {
    --stage: #000000;
    --card: #ffffff;
    --navy: #0b2040;
    --brand-blue: #0a7fc0;
    --text-dark: #14233a;
  }
  * { margin: 0; padding: 0; box-sizing: border-box; }
  html, body {
    width: 1200px; height: 1200px; overflow: hidden;
    background: var(--stage);
  }
  .business-card {
    position: absolute; left: 173px; top: 215px;
    width: 872px; height: 498px;
    background: var(--card); overflow: hidden;
    font-family: 'Montserrat', Arial, sans-serif;
  }
  .card-accents { position: absolute; inset: 0; width: 100%; height: 100%; }
  .label-firma {
    position: absolute; left: 107px; top: 78px;
    font-size: 100px; font-weight: 700; line-height: 1;
    color: var(--navy); letter-spacing: -1px;
  }
  .company-name {
    position: absolute; left: 110px; top: 174px;
    font-size: 36px; font-weight: 400; line-height: 1;
    color: var(--brand-blue); letter-spacing: 0.5px;
  }
  .contact-list { position: absolute; left: 100px; top: 248px; list-style: none; }
  .contact-item {
    display: flex; align-items: center; height: 24px; margin-bottom: 33px;
    font-size: 20px; font-weight: 500; color: var(--text-dark); letter-spacing: 1px;
    white-space: nowrap;
  }
  .contact-icon { width: 24px; height: 24px; margin-right: 17px; flex: none; fill: var(--brand-blue); }
</style>
</head>
<body>
<main class="business-card">
  <svg class="card-accents" viewBox="0 0 1404 802" preserveAspectRatio="none">
    <defs>
      <linearGradient id="accentTop" x1="0" y1="0" x2="1" y2="0">
        <stop offset="0.3" stop-color="#82c0ff"/>
        <stop offset="1" stop-color="#3f88dc"/>
      </linearGradient>
      <linearGradient id="accentBottom" x1="0" y1="1" x2="1" y2="0">
        <stop offset="0" stop-color="#8fdcff"/>
        <stop offset="0.5" stop-color="#82bdfc"/>
        <stop offset="1" stop-color="#3b86d9"/>
      </linearGradient>
    </defs>
    <rect class="accent-top" x="0" y="0" width="470" height="82" fill="url(#accentTop)"
          role="img" aria-label="Blaue Farbfläche, dekorativer Akzent oben links"/>
    <path class="accent-bottom" d="M760 802 L1060 430 H1404 V802 Z" fill="url(#accentBottom)"
          role="img" aria-label="Blaue Verlaufsfläche, dekorativer Akzent unten rechts"/>
  </svg>

  <div class="label-firma">Firma</div>
  <div class="company-name">brandel-advisory</div>

  <ul class="contact-list">
    <li class="contact-item">
      <svg class="contact-icon" viewBox="0 0 24 24" aria-hidden="true"><path d="M12 0C7 0 3.5 3.6 3.5 8.2 3.5 12.5 12 24 12 24s8.5-11.5 8.5-15.8C20.5 3.6 17 0 12 0zm0 11.5a3.4 3.4 0 1 1 0-6.8 3.4 3.4 0 0 1 0 6.8z"/></svg>
      Lindenhang 4, D-73218 Hollenried
    </li>
    <li class="contact-item">
      <svg class="contact-icon" viewBox="0 0 24 24" aria-hidden="true"><path d="M12 1 0 8.5 12 14 24 8.5z"/><path d="M0 10v13h24V10l-12 7z"/></svg>
      Jonas.Wirtel@brandel-advisory.example
    </li>
    <li class="contact-item">
      <svg class="contact-icon" viewBox="0 0 24 24" aria-hidden="true"><path d="M5 0c1 0 1.6.6 2 1.6l1.4 3.6c.3.9 0 1.7-.7 2.3L6 8.8c1.2 3.4 4 6.6 7.3 8.3l1.6-1.5c.7-.6 1.600-.7 2.4-.3l3.3 1.9c.9.5 1.2 1.5.8 2.4l-.8 1.8C20 22.6 18.8 24 17 24 8.8 23 1 15.3 1 5.3 1 2.6 2.7.3 5 0z"/></svg>
      +49 (0) 7354 608193
    </li>
  </ul>
</main>
</body>
</html>
```